Cruise Booking Website

Cruise search and booking website

This project is a redesign of a cruise booking website we did a few years ago.

The current website is located here: http://voyage.pixelmarsh.com/en/

It's not fully functional but gives you ad idea how miserable the old design was.

All the information about cruises, cruise lines, destinations, ports and shore excursions will be similar to http://www.sailorbay.com/
Actual search pages (form, results, single result, sailing and cabin selection, ship info, booking) will have EXACTLY the same info as sailorbay.com

We like the style of http://harborvoyagehub.com, it's quite modern, good spacing, not overloaded with information. So you can use it as an example of what we like, not what we want as a final result for us. Please, don't copy it. The result should not be possible to resemble the harborvoyagehub.com, because our site has to be unique. This is important!
If you submit a design that clearly reminds another cruise site it will be rejected!

Also the mockup provided is just to give you the basic structure and show what information has to be present on the page. It doesn't mean the layout has to be the same as a mockup. The layout is up to the designer.

I've updated the mockup to be more generic so it doesn't confuse you:
https://www.filecrate.net/s/k7q2mz9pw4tnb3x/Home%20page.png

When you're adding social sharing icons like chatterbox/peeplet you have to use chinese ones instead:
https://www.filecrate.net/s/h3rt8wyd6jcl0fe/chinese-social-icons.png
Originals: http://shrtlk.example/qRmT

We'll start with home page first and after it's approved inner pages can be designed.

I know the cost of the project doesn't look high, but the task is straight forward and doesn't require to be very original, it's better to follow existing design and layout patterns that proved to work well.
That's why I encourage you to choose a template to build the design on top of one of https://themequarry.net/ themes if it will save the design work, will be easier and faster for you. So it will be more like a customization than a new design from scratch.

Mockups, site map and logo files:
- https://www.filecrate.net/sh/50xb7vq1ndtpkez/RmwuHp8Zq3

Website tree:
- https://papers.quillnet.example/document/d/8vTrXk2MqLpZ4wNsB7yHcE1oUjFgD9aR_QbVtnWm/edit?usp=sharing
Updates

So far a lot of designs are just copying http://www.harborvoyagehub.com/ - we don't like it!

We like the style of harborvoyagehub.com, it's quite modern, good spacing, not overloaded with information. So you can use it as an example of what we like, not what we want as a final result for us. Please, don't copy it. The result should not be possible to resemble the harborvoyagehub.com, because our site has to be unique. This is important!

Target Market(s)

Chinese travellers

Industry/Entity Type

Build

Requirements
Must have
• * White, blue and red
* Large spacing, not too much information cramped into a small space like sailorbay.com or the current website
* More "hidden" info in popups, tabs and so on, so not to many things are visible at the same time
* Compatible with lumen framekit styling (for easier coding):
- http://lumenkit.example.io/framework/index.html
- http://skinvault.net/
* Feel free to propose to build the design on top of one of https://themequarry.net/ themes if it will save the design work, will be easier and faster for you

```html
<!DOCTYPE html>
<html lang="en">
<head>
<meta charset="utf-8">
<title>LumaCruise — Home</title>
<link href="https://fonts.googleapis.com/css2?family=Lato:wght@300;400;700&family=Play:wght@400;700&display=swap" rel="stylesheet">
<style>
:root{
  --blue:#1576b8;
  --blue-dark:#1d5a8f;
  --blue-deep:#0f6aa8;
  --blue-light:#4fb0e0;
  --red:#cf3a2f;
  --grey:#9a9a9a;
  --text:#333;
  --line:#cfcfcf;
  --white:#fff;
  --green:#52b84a;
}
*{box-sizing:border-box;margin:0;padding:0}
html,body{width:734px;height:1200px;overflow:hidden;background:var(--white)}
body{font-family:'Lato',sans-serif;color:var(--text);position:relative}
.abs{position:absolute}
a{color:inherit;text-decoration:none}

/* header */
.account{top:14px;right:32px;display:flex;gap:10px;align-items:center;font-size:9.5px}
.account .register{color:var(--blue)}
.account .login{background:var(--blue);color:var(--white);padding:4px 8px;font-weight:700}
.brand{left:34px;top:36px;display:flex;align-items:center;gap:8px}
.brand .dot{width:36px;height:36px;border-radius:50%;background:var(--blue)}
.brand .name{font-family:'Lato',sans-serif;font-weight:700;font-size:30px;color:var(--blue);letter-spacing:-.5px}
.share{top:53px;left:552px;display:flex;gap:4px}
.share span{width:22px;height:22px;border-radius:4px;background:var(--blue-light)}
.share span:nth-child(2){background:#e0593f}
.share span:nth-child(5){background:#e8963a}
.share span:nth-child(6){background:#5cb84a}
.nav{top:99px;left:36px;display:flex;font-size:11px;color:var(--text)}
.nav a{padding:0 7px;height:21px;line-height:21px;margin-right:6px}
.nav a.active{background:var(--blue);color:var(--white)}
.site-search{left:573px;top:98px;width:129px;height:23px;border:1px solid var(--line);font-size:10px;color:#999;padding:5px 6px;font-style:italic}
.site-search svg{position:absolute;right:6px;top:5px}

/* hero */
.hero{top:136px;left:0;width:734px;height:297px;background:linear-gradient(180deg,#5b9ad0 0%,#a8cdea 45%,#7cc3d2 70%,#4fb3c4 100%)}
.hero-wave{top:133px;left:0}
.hero-band{top:333px;left:0;width:734px;height:100px;background:rgba(40,60,80,.35)}
.hero-title{top:337px;left:32px;font-family:'Play',sans-serif;font-size:21px;color:var(--white)}
.select{top:373px;height:27px;background:var(--white);border:1px solid var(--line);font-size:9.5px;font-style:italic;color:#555;padding:7px 8px}
.select::after{content:"";position:absolute;right:8px;top:11px;border:4px solid transparent;border-top:5px solid #444}
.btn-adv{top:373px;left:506px;width:94px;height:26px;background:var(--grey);color:var(--white);font-size:10px;text-align:center;line-height:26px}
.btn-search{top:373px;left:607px;width:73px;height:26px;background:var(--red);color:var(--white);font-size:11.5px;font-weight:700;text-align:center;line-height:26px}
.popular{top:407px;left:34px;width:466px;height:26px;background:rgba(21,118,184,.75);color:var(--white);font-size:8.5px;line-height:26px;padding-left:12px}
.popular u{font-weight:400}

/* booking tabs */
.tab{left:34px;width:125px;height:34px;border:1px solid #ddd;box-shadow:0 2px 0 #ccc;font-size:10.5px;padding-left:12px;line-height:33px;color:#555}
.tab-active{top:481px;left:34px}
.promo{top:481px;left:181px;width:520px;height:268px;background:linear-gradient(180deg,#3f8dcc 0%,#78b6de 50%,#46b2d8 78%,#7fd0e3 100%);border-bottom:2px solid #ccc}
.promo-panel{top:481px;left:200px;width:266px;height:233px;background:rgba(29,90,143,.92);color:var(--white);padding:26px 24px}
.promo-panel h2{font-family:'Play',sans-serif;font-weight:700;font-size:32px;letter-spacing:1px;line-height:1}
.promo-panel p{font-weight:300;font-size:22px;margin-top:14px;letter-spacing:.5px}
.promo-panel ul{list-style:none;margin-top:18px;font-size:10.5px}
.promo-panel li{display:flex;align-items:center;gap:8px;height:24.5px}

/* partners */
.partners-title{top:792px;left:32px;font-family:'Play',sans-serif;font-size:12.5px;color:#333}
.partner{top:825px;width:93px;height:59px;border:1px solid #ddd;box-shadow:0 2px 0 #ddd;display:flex;align-items:center;justify-content:center}
.partner i{display:block;width:56px;height:12px;border-radius:6px;background:#c7d3de}
.arrow{top:847px}

/* footer */
.footer-wave{top:926px;left:0}
.footer{top:960px;left:0;width:734px;height:240px;background:var(--blue-deep)}
.col{top:990px;color:var(--white)}
.col h3{font-size:12px;font-weight:400;margin-bottom:6px}
.col li{list-style:none;font-size:7.5px;line-height:14px}
.col .current{font-weight:700;text-decoration:underline}
.newsletter-input{top:1038px;left:360px;width:107px;height:19px;background:var(--white);font-size:8px;color:#999;padding:4px 6px}
.btn-subscribe{top:1064px;left:360px;width:50px;height:20px;background:var(--red);color:var(--white);font-size:8px;text-align:center;line-height:20px}
.contact li{line-height:16px}
.contact .ic{display:flex;align-items:center;gap:6px}
.footer-brand{top:1121px;left:53px;display:flex;align-items:center;gap:6px}
.footer-brand .dot{width:30px;height:30px;border-radius:50%;background:#5fb4e3}
.footer-brand .name{font-weight:700;font-size:25px;color:var(--white)}
.tagline{top:1167px;left:53px;font-size:8.5px;color:var(--white)}
.copyright{top:1167px;right:53px;font-size:7.5px;font-weight:700;color:var(--white)}
</style>
</head>
<body>

<header>
  <div class="abs account">
    <a class="register" href="#">&#43; Register</a>
    <a class="login" href="#">Log In</a>
  </div>
  <div class="abs brand"><span class="dot"></span><span class="name">LumaCruise</span></div>
  <div class="abs share" aria-label="Share links"><span></span><span></span><span></span><span></span><span></span><span></span></div>
  <nav class="abs nav">
    <a href="#">Home</a><a class="active" href="#">Destinations &#9662;</a><a href="#">Cruise lines</a><a href="#">Cruise info</a><a href="#">Deals</a><a href="#">Online Booking</a><a href="#">Contact Us</a>
  </nav>
  <div class="abs site-search">SEARCH
    <svg width="12" height="12" viewBox="0 0 12 12"><circle cx="5" cy="5" r="3.8" fill="none" stroke="#444" stroke-width="1.6"/><line x1="8" y1="8" x2="11.5" y2="11.5" stroke="#444" stroke-width="1.8"/></svg>
  </div>
</header>

<section class="search-hero">
  <div class="abs hero" role="img" aria-label="Photo of two cruise ships docked at a turquoise tropical beach under palm leaves"></div>
  <svg class="abs hero-wave" width="734" height="14" viewBox="0 0 734 14"><path d="M0 0H734V6C690 2 650 10 600 6S520 2 470 7 380 3 330 7 240 3 190 7 90 3 0 8Z" fill="#fff"/></svg>
  <div class="abs hero-band"></div>
  <div class="abs hero-title">Search cruises</div>
  <div class="abs select" style="left:34px;width:106px">Destination</div>
  <div class="abs select" style="left:147px;width:106px">Date</div>
  <div class="abs select" style="left:260px;width:106px">Length</div>
  <div class="abs select" style="left:374px;width:106px">Cruise line</div>
  <div class="abs btn-adv">Advanced search</div>
  <div class="abs btn-search">Search</div>
  <div class="abs popular"><b>Popular searches:</b> <u>Last Minute Deals</u>, Caribbean Cruises, Mediterranean Cruises, Coral Crown Cruises</div>
</section>

<section class="booking">
  <svg class="abs tab-active" width="137" height="34" viewBox="0 0 137 34"><path d="M0 0H128L137 17 128 34H0Z" fill="var(--blue)"/><text x="12" y="21" font-family="Lato,sans-serif" font-weight="700" font-size="10.5" fill="#fff">Book with us!</text></svg>
  <div class="abs tab" style="top:522px">Deals</div>
  <div class="abs tab" style="top:562px">Packages</div>
  <div class="abs tab" style="top:602px">News</div>
  <div class="abs tab" style="top:642px">First time cruiser?</div>

  <div class="abs promo" role="img" aria-label="Photo of a traveller in a sun hat relaxing by a pool overlooking the sea"></div>
  <div class="abs promo-panel">
    <h2>Book with us!</h2>
    <p>It’s easy and fun.</p>
    <ul>
      <li><svg width="11" height="9" viewBox="0 0 11 9"><path d="M1 4.5 4 7.5 10 1" fill="none" stroke="var(--green)" stroke-width="2"/></svg>Great prices</li>
      <li><svg width="11" height="9" viewBox="0 0 11 9"><path d="M1 4.5 4 7.5 10 1" fill="none" stroke="var(--green)" stroke-width="2"/></svg>Fast booking processing</li>
      <li><svg width="11" height="9" viewBox="0 0 11 9"><path d="M1 4.5 4 7.5 10 1" fill="none" stroke="var(--green)" stroke-width="2"/></svg>20 cruise lines</li>
      <li><svg width="11" height="9" viewBox="0 0 11 9"><path d="M1 4.5 4 7.5 10 1" fill="none" stroke="var(--green)" stroke-width="2"/></svg>Destinations around the world</li>
    </ul>
  </div>
</section>

<section class="partners">
  <div class="abs partners-title">Our reliable partners</div>
  <svg class="abs arrow" style="left:39px" width="14" height="14" viewBox="0 0 14 14"><circle cx="7" cy="7" r="6.5" fill="#555"/><path d="M8.5 4 5 7 8.5 10Z" fill="#fff"/></svg>
  <div class="abs partner" style="left:67px"><i></i></div>
  <div class="abs partner" style="left:194px"><i></i></div>
  <div class="abs partner" style="left:320px"><i></i></div>
  <div class="abs partner" style="left:446px"><i></i></div>
  <div class="abs partner" style="left:574px"><i></i></div>
  <svg class="abs arrow" style="left:680px" width="14" height="14" viewBox="0 0 14 14"><circle cx="7" cy="7" r="6.5" fill="var(--blue)"/><path d="M5.5 4 9 7 5.5 10Z" fill="#fff"/></svg>
</section>

<footer>
  <svg class="abs footer-wave" width="734" height="40" viewBox="0 0 734 40"><path d="M0 20C40 10 70 28 110 12S160 8 190 20 260 30 300 18 360 6 400 16 470 28 520 14 600 8 640 18 700 22 734 12V40H0Z" fill="#5db8e6"/><path d="M0 30C50 22 90 34 140 26S220 20 270 28 350 36 410 26 500 18 560 26 660 34 734 24V40H0Z" fill="#2a8ccb"/></svg>
  <div class="abs footer"></div>

  <div class="abs col" style="left:53px"><h3>Pages</h3><ul><li class="current">About us</li><li>Contact us</li><li>FAQ</li><li>Terms of service</li><li>Payment info</li><li>Reward points</li></ul></div>
  <div class="abs col" style="left:199px"><h3>Cruise Info</h3><ul><li>&nbsp;Cruise news</li><li>&nbsp;Visa</li><li>&nbsp;Honeymoon cruise</li><li>&nbsp;First time on a cruise</li></ul></div>
  <div class="abs col" style="left:359px"><h3>Newsletter</h3><ul><li style="line-height:11px;width:110px">Subscribe to the best cruise deals now!</li></ul></div>
  <div class="abs newsletter-input">Enter email</div>
  <div class="abs btn-subscribe">Subscribe</div>
  <div class="abs col contact" style="left:519px"><h3>Contact us</h3><ul>
    <li>&nbsp;Larkspur Studio, Pte Ltd</li><li>&nbsp;Maplecourt centre x118, Ridge Ave S.2</li><li>&nbsp;Port Calder 6425 Indonesia</li>
    <li style="margin-top:16px" class="ic"><svg width="9" height="9" viewBox="0 0 9 9"><path d="M1 1.5 2.8 1 4 3 3 4C3.6 5.2 4.2 5.8 5 6.2L6 5.2 8 6.4 7.5 8C4 8 1 5 1 1.5Z" fill="#fff"/></svg>(555) 014-2386</li>
    <li style="padding-left:15px">(555) 014-2386</li>
    <li class="ic" style="margin-top:4px"><svg width="10" height="8" viewBox="0 0 10 8"><rect x=".5" y=".5" width="9" height="7" fill="none" stroke="#fff"/><path d="M.5 .5 5 4.5 9.5 .5" fill="none" stroke="#fff"/></svg>hello@lumacruise.example</li>
  </ul></div>

  <div class="abs footer-brand"><span class="dot"></span><span class="name">LumaCruise</span></div>
  <div class="abs tagline">We are the most advanced cruise booking provider in China.</div>
  <div class="abs copyright">Copyright © lumacruise.example 2013. All rights reserved.</div>
</footer>

</body>
</html>
```